Lotus Reed Cuisine Road Billboard

Road Billboard I need all of this information on it
Authentic Thai Food Bangkok Style
6.5 Miles on the right
4318 Maple Hollow Rd Otto NC
828-555-0147

```html
<!DOCTYPE html>
<html lang="en">
<head>
<meta charset="utf-8">
<title>Lotus Reed Cuisine – Road Billboard</title>
<link href="https://fonts.googleapis.com/css2?family=Alegreya+Sans:wght@500;700&family=Vollkorn:ital,wght@0,700;1,500&display=swap" rel="stylesheet">
<style>
  :root {
    --page-bg: #e9e6e1;
    --maroon: #6a1511;
    --maroon-deep: #4b0c09;
    --night: #14191b;
    --gold: #f3b71f;
    --cream: #f8e7c6;
    --flame: #e8691c;
    --ember: #9a2d0c;
  }
  * { margin: 0; padding: 0; box-sizing: border-box; }
  html, body { width: 1200px; height: 800px; overflow: hidden; background: var(--page-bg); }
  .canvas {
    width: 1200px; height: 800px;
    display: flex; align-items: center; justify-content: center;
  }
  .billboard {
    position: relative;
    width: 1180px; height: 590px;
    background: linear-gradient(135deg, var(--maroon) 0%, var(--maroon-deep) 100%);
    overflow: hidden;
  }
  .food-photo {
    position: absolute; left: 560px; top: 0; width: 620px; height: 494px;
    background:
      radial-gradient(ellipse 45% 35% at 40% 42%, rgba(120,140,70,0.55), transparent 70%),
      radial-gradient(ellipse 40% 25% at 55% 85%, rgba(232,105,28,0.85), transparent 70%),
      radial-gradient(ellipse 25% 40% at 12% 45%, rgba(232,105,28,0.75), transparent 70%),
      radial-gradient(ellipse 55% 30% at 55% 70%, #2a2d2e, transparent 75%),
      linear-gradient(90deg, var(--maroon-deep) 0%, var(--night) 30%, var(--night) 100%);
  }
  .headline {
    position: absolute; left: 48px; top: 48px;
    font-family: "Vollkorn", Georgia, serif; font-weight: 700;
    color: var(--gold); font-size: 96px; line-height: 0.98;
    letter-spacing: 0.5px; text-transform: uppercase;
  }
  .tagline {
    position: absolute; left: 50px; top: 262px;
    font-family: "Vollkorn", Georgia, serif; font-style: italic; font-weight: 500;
    color: var(--cream); font-size: 70px;
  }
  .divider {
    position: absolute; left: 0; top: 392px; width: 600px; height: 3px;
    background: linear-gradient(90deg, #b8761a, var(--gold) 60%, #b8761a);
  }
  .directions {
    position: absolute; left: 48px; top: 418px;
    display: flex; align-items: center; gap: 10px;
    font-family: "Alegreya Sans", Arial, sans-serif; font-weight: 500;
    color: var(--cream); font-size: 52px;
  }
  .directions svg { width: 36px; height: 30px; }
  .contact-band {
    position: absolute; left: 0; bottom: 0; width: 100%; height: 96px;
    background: var(--maroon-deep);
    display: flex; align-items: center; justify-content: space-between;
    padding: 0 34px 0 48px;
    font-family: "Alegreya Sans", Arial, sans-serif; font-weight: 500;
    color: var(--cream); font-size: 54px;
  }
  .contact-band .address { letter-spacing: -0.3px; }
  .brand {
    position: absolute; right: 44px; top: 118px;
    display: flex; align-items: center; gap: 10px;
    font-family: "Alegreya Sans", Arial, sans-serif; font-weight: 700;
    color: var(--gold); font-size: 26px;
  }
  .brand-dot { width: 16px; height: 16px; border-radius: 50%; background: var(--gold); }
</style>
</head>
<body>
<main class="canvas">
  <section class="billboard">
    <div class="food-photo" role="img" aria-label="Shrimp and greens tossed above a flaming wok against a dark background"></div>

    <h1 class="headline">Authentic<br>Thai Food</h1>
    <p class="tagline">Bangkok Style</p>
    <div class="divider"></div>
    <p class="directions">6.5 Miles on the Right
      <svg viewBox="0 0 36 30" aria-hidden="true"><path d="M2 15h28M20 5l11 10-11 10" fill="none" stroke="#f8e7c6" stroke-width="4" stroke-linecap="round" stroke-linejoin="round"/></svg>
    </p>

    <div class="brand"><span class="brand-dot"></span><span class="brand-name">Lotus Reed Cuisine</span></div>

    <footer class="contact-band">
      <span class="address">4318 Maple Hollow Rd, Otto, NC</span>
      <span class="phone">828-555-0147</span>
    </footer>
  </section>
</main>
</body>
</html>
```